Prestige Car Bodyshop Business Card

We are a car bodyshop based in the UK. Our customer base is mainly prestige high-value vehicles. I am looking for a classy and stylish business card design for my staff to give out to customers, with their direct email and phone number, as well as our main email and phone number with address details

I am also looking to have a general business card design with just our main company address and contact details, but also have a space to add a manufacturer approval logo (i.e Velmora, Orek, Tovalo etc... logo) in the corner somewhere.

I do not particularly want any outlines or pictures of cars on the card, I would just like a quality high-end look.

Please feel free to get in touch if you have any questions or queries?

Many Thanks

Malcolm

Target Market(s)

Prestige vehicle owners

Industry/Entity Type

Automotive

Contact Information for Business Card

I am looking for a classy and stylish business card design for my staff to give out to customers, with their direct email and phone number, as well as our main email and phone number with address details

Font styles to use
Sans Serif

Colors

Designer to choose colors to be used in the design.

Requirements
Nice to have
• I do not particularly want any outlines or pictures of cars on the card, I would just like a quality high-end look.

```html
<!DOCTYPE html>
<html lang="en">
<head>
<meta charset="utf-8">
<title>Harland Accident Repair Centre – Business Cards</title>
<link rel="stylesheet" href="https://fonts.googleapis.com/css2?family=Alegreya+Sans:wght@300;400;500&display=swap">
<style>
  :root {
    --navy: #0b1f7c;
    --bright: #1d4fe2;
    --orange: #ff6a13;
    --ink: #1a1a1a;
    --paper: #ffffff;
    --page: #ffffff;
  }
  * { box-sizing: border-box; margin: 0; padding: 0; }
  html, body { width: 874px; height: 1200px; overflow: hidden; background: var(--page); }
  body { position: relative; font-family: "Alegreya Sans", sans-serif; }

  .card {
    position: absolute;
    width: 803px; height: 472px;
    background: var(--paper);
    border: 1.5px solid var(--ink);
    box-shadow: 22px 24px 22px rgba(0,0,0,.32);
  }
  .card--company { left: 2px; top: 2px; }
  .card--staff { left: 6px; top: 674px; }

  .brand { position: absolute; left: 49px; top: 32px; display: flex; align-items: center; }
  .brand__dot {
    width: 102px; height: 102px; border-radius: 50%;
    background: radial-gradient(circle at 40% 35%, #2a63f0, var(--navy) 85%);
  }
  .brand__text { margin-left: 14px; color: var(--navy); font-weight: 400; }
  .brand__name { font-size: 44px; line-height: 1; letter-spacing: -0.5px; }
  .brand__rule { height: 2px; background: var(--navy); width: 191px; margin: 6px 0 4px; }
  .brand__tag { font-size: 15.5px; letter-spacing: 0.2px; }

  .tile {
    position: absolute;
    display: flex; align-items: center; justify-content: center;
    background: var(--navy);
    color: var(--orange);
    font-weight: 300;
    text-align: center;
  }
  .tile--bright { background: var(--bright); }
  .tile svg { fill: var(--orange); }

  .address-lines { font-size: 18px; line-height: 1.15; letter-spacing: 0.2px; }
  .contact-line { font-size: 25px; letter-spacing: 0.4px; }
  .staff-line { font-size: 34px; letter-spacing: 0.3px; }
  .staff-email { font-size: 22px; }

  .maker-mark {
    position: absolute; left: 76px; top: 330px; width: 192px;
    text-align: center; color: var(--ink);
    font-size: 28px; font-weight: 500; letter-spacing: 4px;
  }
</style>
</head>
<body>

<section class="card card--company">
  <div class="brand">
    <div class="brand__dot"></div>
    <div class="brand__text">
      <div class="brand__name">HARLAND</div>
      <div class="brand__rule"></div>
      <div class="brand__tag">ACCIDENT REPAIR CENTRE</div>
    </div>
  </div>

  <div class="tile" style="left:351px;top:219px;width:76px;height:76px">
    <svg width="30" height="44" viewBox="0 0 30 44"><path d="M15 0C6.7 0 0 6.7 0 15c0 11 15 29 15 29s15-18 15-29C30 6.7 23.3 0 15 0zm0 21a6 6 0 1 1 0-12 6 6 0 0 1 0 12z"/></svg>
  </div>
  <div class="tile address-lines" style="left:438px;top:219px;width:322px;height:76px">
    Eastfield Road, Kingsmead,<br>Hallow, Bristol BS31 9QT,<br>United Kingdom
  </div>

  <div class="tile tile--bright" style="left:453px;top:302px;width:57px;height:57px">
    <svg width="30" height="20" viewBox="0 0 30 20"><path d="M0 0h30v20H0z"/><path d="M1 1l14 10L29 1" fill="none" stroke="#1d4fe2" stroke-width="2"/></svg>
  </div>
  <div class="tile tile--bright contact-line" style="left:518px;top:302px;width:242px;height:57px;font-size:21px">
    info@harlandrepairs.co.uk
  </div>

  <div class="tile" style="left:453px;top:365px;width:57px;height:57px">
    <svg width="26" height="26" viewBox="0 0 24 24"><path d="M6.6 10.8a15.1 15.1 0 0 0 6.6 6.6l2.2-2.2a1 1 0 0 1 1-.25 11.4 11.4 0 0 0 3.6.57 1 1 0 0 1 1 1V20a1 1 0 0 1-1 1A17 17 0 0 1 3 4a1 1 0 0 1 1-1h3.5a1 1 0 0 1 1 1c0 1.25.2 2.45.57 3.57a1 1 0 0 1-.25 1z"/></svg>
  </div>
  <div class="tile contact-line" style="left:518px;top:365px;width:242px;height:57px">
    0117 496 0721
  </div>
</section>

<section class="card card--staff">
  <div class="brand" style="left:42px;top:22px">
    <div class="brand__dot"></div>
    <div class="brand__text">
      <div class="brand__name">HARLAND</div>
      <div class="brand__rule"></div>
      <div class="brand__tag">ACCIDENT REPAIR CENTRE</div>
    </div>
  </div>

  <div class="tile" style="left:351px;top:126px;width:76px;height:76px">
    <svg width="34" height="40" viewBox="0 0 34 40"><path d="M17 3a10 10 0 0 1 10 10c0 6-4 12-10 14-6-2-10-8-10-14A10 10 0 0 1 17 3z" fill="none" stroke="#ff6a13" stroke-width="4"/><path d="M3 37c2-6 8-8 14-8s12 2 14 8z" fill="none" stroke="#ff6a13" stroke-width="4" stroke-linejoin="round"/></svg>
  </div>
  <div class="tile staff-line" style="left:438px;top:126px;width:322px;height:76px">Staff Name</div>

  <div class="tile" style="left:351px;top:210px;width:76px;height:76px">
    <svg width="44" height="40" viewBox="0 0 44 40"><path d="M22 0L0 20h6v20h12V28h8v12h12V20h6z"/></svg>
  </div>
  <div class="tile staff-line" style="left:438px;top:210px;width:322px;height:76px">Staff address</div>

  <div class="tile tile--bright" style="left:453px;top:293px;width:57px;height:57px">
    <svg width="30" height="20" viewBox="0 0 30 20"><path d="M0 0h30v20H0z"/><path d="M1 1l14 10L29 1" fill="none" stroke="#1d4fe2" stroke-width="2"/></svg>
  </div>
  <div class="tile tile--bright staff-email" style="left:518px;top:293px;width:242px;height:57px;font-size:19px">
    staff@harlandrepairs.co.uk
  </div>

  <div class="tile" style="left:453px;top:356px;width:57px;height:57px">
    <svg width="26" height="26" viewBox="0 0 24 24"><path d="M6.6 10.8a15.1 15.1 0 0 0 6.6 6.6l2.2-2.2a1 1 0 0 1 1-.25 11.4 11.4 0 0 0 3.6.57 1 1 0 0 1 1 1V20a1 1 0 0 1-1 1A17 17 0 0 1 3 4a1 1 0 0 1 1-1h3.5a1 1 0 0 1 1 1c0 1.25.2 2.45.57 3.57a1 1 0 0 1-.25 1z"/></svg>
  </div>
  <div class="tile contact-line" style="left:518px;top:356px;width:242px;height:57px">
    0117 496 0721
  </div>

  <div class="maker-mark">STANMERE</div>
</section>

</body>
</html>
```